Orvex Panel Flyer

I need a flyer designed for our Orvex Panel software service. Basically most of the content that is on the website (orvexpanel.com.au) but I have uploaded a couple of source files as well. Please continue with this blue colour scheme

Target Market(s)

Business owners

Industry/Entity Type

Software

Font styles to use
Sans Serif

Colors
0456a4

Requirements
Must have
• Content from orvexpanel.com.au and similar theme

```html
<!DOCTYPE html>
<html lang="en">
<head>
<meta charset="utf-8">
<title>Orvex Panel Flyer</title>
<link href="https://fonts.googleapis.com/css2?family=Open+Sans:wght@300;400;600;700;800&display=swap" rel="stylesheet">
<style>
  :root {
    --brand-blue: #0456a4;
    --sky-blue: #2a8fd0;
    --navy: #1f3f9a;
    --violet: #3a2f9a;
    --light-blue: #3d9ad8;
    --ink-gray: #555a63;
    --charcoal: #2b2b2d;
    --paper: #ffffff;
    --backdrop: #e6e7e9;
  }
  * { margin: 0; padding: 0; box-sizing: border-box; }
  html, body {
    width: 1200px; height: 1200px; overflow: hidden;
    background: var(--backdrop);
    font-family: "Open Sans", Arial, sans-serif;
  }
  .flyer {
    position: absolute; left: 204px; top: 40px;
    width: 792px; height: 1120px;
    background: var(--paper);
    overflow: hidden;
    box-shadow: 0 6px 24px rgba(0,0,0,.12);
  }
  .flyer-shapes, .hero-photo { position: absolute; left: 0; top: 0; }
  .headline { position: absolute; left: 48px; top: 44px; line-height: 1; }
  .headline .kicker { display: block; color: var(--sky-blue); font-weight: 600; font-size: 29px; letter-spacing: .5px; }
  .headline .soft { color: var(--ink-gray); font-weight: 300; font-size: 32px; letter-spacing: .5px; }
  .headline .strong {
    font-weight: 800; color: var(--navy);
    background: linear-gradient(90deg, var(--navy), var(--brand-blue) 60%, var(--sky-blue));
    -webkit-background-clip: text; background-clip: text; -webkit-text-fill-color: transparent;
  }
  .headline .line { display: block; margin-top: 6px; }
  .headline .pulse { font-size: 62px; }
  .headline .business { font-size: 76px; letter-spacing: 1px; }
  .brand-name {
    position: absolute; right: 34px; top: 52px;
    color: var(--paper); font-weight: 700; font-size: 22px; letter-spacing: 1px;
    display: flex; align-items: center; gap: 8px;
  }
  .brand-name .dot { width: 12px; height: 12px; border-radius: 50%; background: var(--paper); }
  .feature { position: absolute; display: flex; gap: 14px; align-items: flex-start; }
  .feature-icon {
    flex: none; width: 58px; height: 58px; border-radius: 50%;
    background: var(--paper); border: 3px solid var(--brand-blue);
    display: flex; align-items: center; justify-content: center;
    box-shadow: 0 2px 6px rgba(0,0,0,.2);
  }
  .feature h3 { color: var(--brand-blue); font-weight: 600; font-size: 19px; line-height: 1.1; }
  .feature p { color: var(--ink-gray); font-size: 13px; line-height: 1.22; margin-top: 2px; }
  .cta {
    position: absolute; left: 36px; top: 660px;
    color: var(--paper); font-weight: 600; font-size: 23px; letter-spacing: .5px;
  }
  .about { position: absolute; left: 36px; top: 740px; width: 350px; color: var(--paper); }
  .about h2 { font-size: 20px; font-weight: 600; margin-bottom: 10px; }
  .about p { font-size: 14.5px; line-height: 1.35; font-weight: 300; margin-bottom: 14px; }
  .divider { position: absolute; left: 404px; top: 728px; width: 1.5px; height: 240px; background: rgba(255,255,255,.8); }
  .highlights { position: absolute; left: 424px; top: 712px; width: 340px; color: var(--paper); }
  .highlights h4 { font-size: 15px; font-weight: 700; }
  .highlights p { font-size: 14px; line-height: 1.3; font-weight: 300; margin-bottom: 12px; }
</style>
</head>
<body>
<article class="flyer">
  <svg class="flyer-shapes" width="792" height="1120" viewBox="0 0 792 1120" aria-hidden="true">
    <defs>
      <linearGradient id="corner-blue" x1="0" y1="0" x2="1" y2="1">
        <stop offset="0" stop-color="#3a3fa6"/><stop offset="1" stop-color="#2a8fd0"/>
      </linearGradient>
      <linearGradient id="base-blue" x1="0" y1="1" x2="1" y2="0">
        <stop offset="0" stop-color="#3a2f9a"/><stop offset=".5" stop-color="#2f5bb8"/><stop offset="1" stop-color="#3d9ad8"/>
      </linearGradient>
    </defs>
    <polygon points="540,0 792,0 792,335" fill="url(#corner-blue)"/>
    <polygon points="495,0 520,0 792,362 792,398" fill="url(#corner-blue)"/>
    <polygon points="0,712 600,700 792,620 792,1120 0,1120" fill="url(#base-blue)"/>
    <polygon points="0,640 552,640 604,700 0,712" fill="var(--charcoal)"/>
  </svg>

  <svg class="hero-photo" width="792" height="1120" viewBox="0 0 792 1120" role="img" aria-label="Photo of a businessman in a suit and glasses reading his smartphone in a cafe">
    <defs>
      <linearGradient id="photo-tones" x1="0" y1="0" x2="1" y2="1">
        <stop offset="0" stop-color="#6b4a2e"/><stop offset=".35" stop-color="#2a2a2e"/><stop offset="1" stop-color="#141518"/>
      </linearGradient>
    </defs>
    <polygon points="0,288 132,262 520,640 0,640" fill="url(#photo-tones)"/>
  </svg>

  <header class="headline">
    <span class="kicker">KEEP YOUR FINGER</span>
    <span class="line"><span class="soft">ON THE </span><span class="strong pulse">PULSE</span></span>
    <span class="line soft">OF YOUR</span>
    <span class="line strong business">BUSINESS</span>
  </header>

  <div class="brand-name"><span class="dot"></span>ORVEX PANEL</div>

  <section class="feature" style="left:170px; top:268px; width:500px;">
    <span class="feature-icon"><svg width="28" height="28" viewBox="0 0 28 28"><g fill="var(--charcoal)"><rect x="3" y="18" width="4" height="7"/><rect x="9" y="14" width="4" height="11"/><rect x="15" y="10" width="4" height="15"/><rect x="21" y="6" width="4" height="19"/></g><path d="M3 14 L12 8 L17 11 L25 3" stroke="var(--charcoal)" stroke-width="2" fill="none"/></svg></span>
    <div><h3>Performance</h3><p>Less time collecting data; more time coaching your team. Orvex Panel has been proven to shave precious hours out of a managers day.</p></div>
  </section>

  <section class="feature" style="left:240px; top:356px; width:500px;">
    <span class="feature-icon"><svg width="24" height="30" viewBox="0 0 24 30"><rect x="4" y="2" width="16" height="26" rx="3" stroke="var(--charcoal)" stroke-width="2" fill="none"/><line x1="10" y1="24" x2="14" y2="24" stroke="var(--charcoal)" stroke-width="2"/></svg></span>
    <div><h3>Mobile friendly</h3><p>All our reports are fully optimised to be viewed on any platform including smartphones, tablets and PCs</p></div>
  </section>

  <section class="feature" style="left:340px; top:444px; width:428px;">
    <span class="feature-icon"><svg width="28" height="28" viewBox="0 0 28 28"><circle cx="14" cy="15" r="10" stroke="var(--charcoal)" stroke-width="2" fill="none"/><path d="M14 9 V15 L18 18" stroke="var(--charcoal)" stroke-width="2" fill="none"/><path d="M4 6 L8 3 M24 6 L20 3" stroke="var(--charcoal)" stroke-width="2"/></svg></span>
    <div><h3>Responsive</h3><p>We are always on top of the current priorities in the channel and respond quickly to give you the insights you need to be proactive and win.</p></div>
  </section>

  <section class="feature" style="left:446px; top:530px; width:312px;">
    <span class="feature-icon"><svg width="28" height="28" viewBox="0 0 28 28"><circle cx="14" cy="14" r="5" stroke="var(--charcoal)" stroke-width="2" fill="none"/><circle cx="14" cy="14" r="10" stroke="var(--charcoal)" stroke-width="3" stroke-dasharray="4 3" fill="none"/></svg></span>
    <div><h3>Customisable</h3><p>We offer a range of customised reporting solutions including traffic reporting, commission trackers, inventory management and just about anything else.</p></div>
  </section>

  <div class="cta">Contact us for a free trial</div>

  <section class="about">
    <h2>About us</h2>
    <p>We specialise in providing reporting and staff performance management tools to the Vantel Licensed Store (VLS) channel.</p>
    <p>With our Orvex Panel service, our aim to help you boost performance in your teams and increase efficiency by providing comprehensive reporting and performance management tools that help you keep your finger on the pulse of your business.</p>
  </section>

  <div class="divider"></div>

  <section class="highlights">
    <h4>Know your numbers.</h4>
    <p>Simple and interactive reports that highlight the main opportunities in your sales team.</p>
    <h4>Customer experience insights.</h4>
    <p>Gain brilliant insights into the customer experience through a range of reports that breath life into your NPS and RAD data</p>
    <h4>Custom built solutions.</h4>
    <p>We offer a wide range of customised reporting solutions including staff commission trackers, live BOH TV screens and team product targets.</p>
  </section>
</article>
</body>
</html>
```